Storm Restoration Contractor needs a professional letterhead design

Looking for a professional letterhead design. Not looking for your cheapo MS Word standard ones that are readily available. Dont want it to be cookie cutter look like ones readily available online. We just recently changed our logo and want to freshen up all our documents. Our company handles restoring a property back to a pre-loss condition after a storm damages it. For example, wind, hail, flood, fire losses.

Target Market(s)

Property Owners, Homeowners, Property Owners, Commercial Property Owners, Property Management Companies

Industry/Entity Type

Construction Company

Requirements
Must have
• Professional, Use 1 of 2 logo options
• Storm Restoration, Roofing, Siding, Windows

```html
<!DOCTYPE html>
<html lang="en">
<head>
<meta charset="utf-8">
<title>Stormline Exteriors Letterhead</title>
<link href="https://fonts.googleapis.com/css2?family=Open+Sans:wght@400;600;700&display=swap" rel="stylesheet">
<style>
  :root {
    --backdrop: #cfc4c2;
    --paper: #ffffff;
    --brand-blue: #1f73c4;
    --ink: #3a3a3a;
    --ink-soft: #555555;
    --band-grey: #5a5d63;
    --watermark: #eef2f8;
  }
  * { margin: 0; padding: 0; box-sizing: border-box; }
  html, body {
    width: 1200px; height: 785px; overflow: hidden;
    background: var(--backdrop);
    font-family: "Open Sans", Arial, sans-serif;
  }
  .letterhead {
    position: absolute; left: 337px; top: 20px;
    width: 527px; height: 745px;
    background: var(--paper);
    box-shadow: 0 6px 18px rgba(0,0,0,.18);
    overflow: hidden;
  }
  .watermark { position: absolute; left: 84px; top: 190px; width: 360px; height: 360px; }
  .brand {
    position: absolute; top: 34px; right: 40px;
    display: flex; align-items: center; gap: 8px;
    color: var(--brand-blue); font-weight: 700; font-size: 13px; letter-spacing: .5px;
  }
  .brand-dot { width: 22px; height: 22px; border-radius: 50%; background: var(--brand-blue); }
  .letter { position: absolute; left: 48px; top: 100px; width: 420px; color: var(--ink-soft); font-size: 9.5px; line-height: 1.5; }
  .salutation { font-weight: 700; font-size: 11px; color: var(--ink); margin-bottom: 8px; }
  .letter p { margin-bottom: 9px; }
  .signature { position: absolute; left: 52px; top: 400px; width: 80px; height: 34px; background: linear-gradient(90deg,#e6e6e6,#f4f4f4); border-radius: 3px; }
  .footer { position: absolute; left: 40px; bottom: 56px; display: flex; gap: 26px; font-size: 9.5px; color: var(--ink); line-height: 1.55; }
  .footer-name { color: var(--brand-blue); font-weight: 600; }
  .contact-list { list-style: none; }
  .contact-list li { display: flex; align-items: center; gap: 6px; }
  .contact-icon { width: 11px; height: 11px; }
  .bottom-band { position: absolute; left: 0; right: 0; bottom: 18px; height: 6px; background: var(--band-grey); }
  .web-tab {
    position: absolute; right: 0; bottom: 14px; width: 200px; height: 20px;
    background: var(--brand-blue); color: #fff; font-size: 9.5px;
    display: flex; align-items: center; justify-content: center;
    clip-path: polygon(12px 0, 100% 0, 100% 100%, 0 100%);
  }
</style>
</head>
<body>
  <main class="letterhead">
    <svg class="watermark" viewBox="0 0 360 360" aria-hidden="true">
      <circle cx="180" cy="180" r="160" fill="none" stroke="var(--watermark)" stroke-width="26"/>
    </svg>

    <header class="brand">
      <span class="brand-dot"></span>
      <span class="brand-name">STORMLINE EXTERIORS</span>
    </header>

    <section class="letter">
      <p class="salutation">Dear Mr. Carter,</p>
      <p>Lorem Ipsum is simply dummy text of the printing and typesetting industry. Lorem Ipsum has been the industry's standard dummy text ever since the 1500s, when an unknown printer took a galley of type and scrambled it to make a type specimen book. It has survived not only five centuries, but also the leap into electronic typesetting, remaining essentially unchanged.</p>
      <p>The standard chunk of Lorem Ipsum used since the 1500s is reproduced below for those interested. Sections 1.10.32 and 1.10.33 from "de Finibus Bonorum et Malorum" by Cicero are also reproduced in their exact original form, accompanied by English versions from the 1914 translation by H. Rackham.</p>
      <p>Lorem Ipsum is simply dummy text of the printing and typesetting industry. Lorem Ipsum has been the industry's standard dummy text ever since the 1500s, when an unknown printer took a galley of type and scrambled it to make a type specimen book. It has survived not only five centuries, but also the leap into electronic typesetting, remaining essentially unchanged. It was popularised in the</p>
    </section>

    <div class="signature" role="img" aria-label="Handwritten signature of the sender"></div>

    <footer class="footer">
      <address class="footer-address" style="font-style:normal">
        <div class="footer-name">Stormline Exteriors</div>
        <div>2250 Harbor Crest Lane,</div>
        <div>Fairview, CA 95010</div>
      </address>
      <ul class="contact-list">
        <li>
          <svg class="contact-icon" viewBox="0 0 12 12"><circle cx="6" cy="6" r="6" fill="var(--brand-blue)"/><path d="M4 3.2l1 1.4-.6.7c.4.9 1 1.5 1.9 1.9l.7-.6 1.4 1-.5 1.2C5.6 8.6 3.4 6.4 3.2 4.2z" fill="#fff"/></svg>
          (555) 204-1187
        </li>
        <li>
          <svg class="contact-icon" viewBox="0 0 12 12"><circle cx="6" cy="6" r="6" fill="var(--brand-blue)"/><rect x="3.3" y="4.5" width="5.4" height="3.5" fill="#fff"/><rect x="4.2" y="3" width="3.6" height="1.5" fill="#fff"/></svg>
          (555) 204-1188
        </li>
        <li>
          <svg class="contact-icon" viewBox="0 0 12 12"><circle cx="6" cy="6" r="6" fill="var(--brand-blue)"/><rect x="3" y="4" width="6" height="4" fill="#fff"/><path d="M3 4l3 2.2L9 4" fill="none" stroke="var(--brand-blue)" stroke-width=".8"/></svg>
          info@stormlineexteriors.com
        </li>
      </ul>
    </footer>

    <div class="bottom-band"></div>
    <div class="web-tab">www.stormlineexteriors.com</div>
  </main>
</body>
</html>
```